Bespoke Branding Agency "Tidal Marks" seeks uplifting wordpress site

Looking for a SIMPLE, CLEAN, easy to manage wordpress site for our start-up Branding business. Our company is "Tidal Marks" and the site should reflect our vision.

We formed the company after making the decision never to work the average 9 to 5 work life again. We have vowed to never work in traditional corporate culture again. We are committed to a happier life with reduced stress and increased job satisfaction.

We want to build brands that make people happy.

We want to work with people who believe that you don’t have to be an asshole to be successful.

We believe that success should not be measured in monetary terms, but rather in happiness scores.

We believe in the Corwin Ashdale song lyric "Folks ought to grin often”.

We love sunflowers.

We prefer brevity over long wind.

We are motivated by creativity not money.

We love spending time with friends and family, and see this as our main priority in life.

We know life is short.

Industry/Entity Type

Business

```html
<!DOCTYPE html>
<html lang="en">
<head>
<meta charset="utf-8">
<title>Tidal Marks — Contact</title>
<link rel="stylesheet" href="https://fonts.googleapis.com/css2?family=Arimo:wght@400;700&family=Open+Sans:wght@400;600&display=swap">
<style>
  :root {
    --brand-pink: #ee175a;
    --field-white: #ffffff;
    --field-border: #2b2b2b;
    --placeholder-grey: #9a9a9a;
    --button-ink: #333333;
    --footer-dark: #242424;
    --footer-dark-edge: #1b1b1b;
    --legal-bar: #121212;
    --social-disc: #161616;
    --text-light: #ffffff;
  }
  * { box-sizing: border-box; margin: 0; padding: 0; }
  html, body { width: 1200px; height: 900px; overflow: hidden; background: var(--legal-bar); }
  .page { position: relative; width: 1200px; height: 900px; overflow: hidden; }

  .contact-band { position: absolute; left: 0; top: 0; width: 1200px; height: 265px; background: var(--brand-pink); }
  .field {
    position: absolute; background: var(--field-white);
    border: 2px solid var(--field-border);
  }
  .field--message { left: 44px; top: -10px; width: 525px; height: 184px; }
  .field--name { left: 628px; top: -40px; width: 525px; height: 53px; }
  .field--email { left: 628px; top: 23px; width: 525px; height: 65px; }
  .field-placeholder {
    position: absolute; left: 23px; top: 18px;
    font: 400 22px/1 "Open Sans", sans-serif; color: var(--placeholder-grey);
  }
  .send-button {
    position: absolute; left: 628px; top: 103px; width: 241px; height: 70px;
    background: var(--field-white); border: 2px solid var(--field-border);
    display: flex; align-items: center; justify-content: center;
    font: 600 17px/1 "Open Sans", sans-serif; color: var(--button-ink);
  }

  .site-footer { position: absolute; left: 0; top: 265px; width: 1200px; height: 518px; }
  .footer-texture {
    position: absolute; inset: 0;
    background: radial-gradient(ellipse at 50% 40%, var(--footer-dark) 0%, var(--footer-dark-edge) 100%);
  }
  .brand-mark {
    position: absolute; left: 533px; top: 81px; width: 130px; height: 130px;
    border-radius: 50%; background: var(--brand-pink);
    display: flex; align-items: center; justify-content: center; text-align: center;
    font: 700 20px/1.1 "Arimo", sans-serif; color: var(--text-light); letter-spacing: 0.5px;
  }
  .brand-name {
    position: absolute; left: 0; width: 1200px; top: 248px; text-align: center;
    font: 400 45px/1 "Arimo", sans-serif; color: var(--text-light);
  }
  .brand-address {
    position: absolute; left: 0; width: 1200px; top: 313px; text-align: center;
    font: 400 34px/42px "Arimo", sans-serif; color: var(--text-light); font-style: normal;
  }
  .social-links { position: absolute; left: 504px; top: 426px; display: flex; gap: 11px; }
  .social-link {
    width: 54px; height: 54px; border-radius: 50%; background: var(--social-disc);
    display: flex; align-items: center; justify-content: center;
  }
  .social-link svg { width: 22px; height: 22px; fill: none; stroke: var(--text-light); stroke-width: 2.2; stroke-linecap: round; stroke-linejoin: round; }

  .legal-bar { position: absolute; left: 0; top: 783px; width: 1200px; height: 117px; background: var(--legal-bar); }
  .copyright {
    position: absolute; left: 0; width: 1200px; top: 42px; text-align: center;
    font: 400 14px/1 "Arimo", sans-serif; color: var(--text-light);
  }
</style>
</head>
<body>
<div class="page">
  <section class="contact-band">
    <div class="field field--message"></div>
    <div class="field field--name"></div>
    <div class="field field--email"><span class="field-placeholder">Email</span></div>
    <div class="send-button">SEND MESSAGE</div>
  </section>

  <footer class="site-footer">
    <div class="footer-texture" role="img" aria-label="Dark woven fabric texture"></div>
    <div class="brand-mark">TIDAL<br>MARKS</div>
    <h2 class="brand-name">TIDAL MARKS</h2>
    <address class="brand-address">4120 Meadow Lane |Suite 310<br>Brookvale Park,OS | 55184</address>
    <nav class="social-links" aria-label="Social profiles">
      <span class="social-link" aria-label="Email">
        <svg viewBox="0 0 24 24"><rect x="3" y="6" width="18" height="12" rx="1"/><path d="M3 7l9 6 9-6"/></svg>
      </span>
      <span class="social-link" aria-label="Website">
        <svg viewBox="0 0 24 24"><circle cx="12" cy="12" r="9"/><path d="M3 12h18M12 3c3 3 3 15 0 18M12 3c-3 3-3 15 0 18"/></svg>
      </span>
      <span class="social-link" aria-label="Share">
        <svg viewBox="0 0 24 24"><circle cx="6" cy="12" r="2.5"/><circle cx="18" cy="6" r="2.5"/><circle cx="18" cy="18" r="2.5"/><path d="M8.2 10.8l7.6-3.6M8.2 13.2l7.6 3.6"/></svg>
      </span>
    </nav>
  </footer>

  <div class="legal-bar">
    <p class="copyright">Copyright © 2013. All rights reserved</p>
  </div>
</div>
</body>
</html>
```